NEW FACEBOOK AD CREATIVES FOR MARKETING AGENCY

We need one single static image AND a Carousel Ad Design With 5 Cards Total in it.

We advertise a SaaS Product that teaches businesses how to use incentive based marketing to get more sales and leads.

Using our service businesses can give away smart devices like smartwatches, earpods, mp4 players, tablets, etc. as a gift bonus along with their product or service as an added value benefit to help them create more attractive offers and to get more sales.

I have attached two designs that get me my best results on facebook ads so far so I want to create something very similar with a different look and showcasing 3-4 of the items I have attached images for.

CONTENT & INSTRUCTIONS:
MAIN TEXT: TRIPLE YOUR SALES OFFERING FREE SMART DEVICES AS A BONUS FOR BUYING YOUR PRODUCT OR SERVICE

Target Market(s)

ENTREPRENEURS, INVESTORS, BUSINESS OWNERS, MEDIA AGENCIES, BROKERAGES

Industry/Entity Type

marketing gifting

Requirements
Must have
• must match color scheme of website www.brightlooprewardhub.biz as this is where they will be redirected to when they click.
Nice to have
• the ads must be 1080x1080 Static newsfeed ad and carousel ads

```html
<!DOCTYPE html>
<html lang="en">
<head>
<meta charset="utf-8">
<title>Triple Your Sales – Smart Device Bonus Ad</title>
<link rel="stylesheet" href="https://fonts.googleapis.com/css2?family=Anton&family=Roboto:wght@700;900&display=swap">
<style>
  :root {
    --stage: #303030;
    --paper: #f8f9fa;
    --sky: #85c8fb;
    --sky-pale: #ddeefd;
    --ink: #272727;
    --flame: #ff3d00;
    --white: #ffffff;
    --accent-orange: #ff7a1a;
    --dot-grey: #c9ced4;
  }
  * { box-sizing: border-box; margin: 0; padding: 0; }
  html, body {
    width: 1166px;
    height: 1200px;
    overflow: hidden;
    background: var(--stage);
  }
  .ad {
    position: absolute;
    left: 125px;
    top: 122px;
    width: 952px;
    height: 952px;
    overflow: hidden;
    background: var(--paper);
  }
  .ad__backdrop {
    position: absolute;
    inset: 0;
  }
  .headline {
    position: absolute;
    left: 0;
    right: 0;
    top: 72px;
    text-align: center;
    font-family: "Anton", Impact, sans-serif;
    color: var(--ink);
    text-transform: none;
    line-height: 1;
  }
  .headline__lead {
    display: block;
    font-size: 34px;
    letter-spacing: 0.2px;
  }
  .headline__main {
    display: block;
    margin-top: 4px;
    font-size: 84px;
    color: var(--flame);
    letter-spacing: 0.5px;
  }
  .headline__offer {
    display: block;
    margin-top: 2px;
    font-size: 49px;
    letter-spacing: 0.6px;
  }
  .headline__detail {
    display: block;
    margin-top: 10px;
    font-size: 35px;
    line-height: 44px;
    letter-spacing: 0.3px;
  }
  .cta-band {
    position: absolute;
    left: 0;
    right: 0;
    top: 850px;
    bottom: 0;
    background: var(--paper);
  }
  .cta-button {
    position: absolute;
    left: 253px;
    top: 872px;
    width: 446px;
    height: 62px;
    border-radius: 8px;
    background: var(--flame);
    box-shadow: 0 6px 10px rgba(0, 0, 0, 0.22);
    color: var(--white);
    font-family: "Roboto", Arial, sans-serif;
    font-weight: 700;
    font-size: 28px;
    letter-spacing: 0.3px;
    display: flex;
    align-items: center;
    justify-content: center;
  }
</style>
</head>
<body>
  <main class="ad">
    <svg class="ad__backdrop" width="952" height="952" viewBox="0 0 952 952" aria-hidden="true">
      <!-- large sky arch -->
      <ellipse cx="476" cy="780" rx="760" ry="770" fill="var(--sky)"/>
      <!-- pale lower circle -->
      <circle cx="476" cy="905" r="455" fill="var(--sky-pale)"/>
      <!-- inner sky circle -->
      <circle cx="476" cy="905" r="250" fill="var(--sky)"/>

      <!-- dot grid top right -->
      <g class="dot-grid" fill="var(--dot-grey)">
        <circle cx="828" cy="36" r="2.2"/><circle cx="842" cy="36" r="2.2"/><circle cx="856" cy="36" r="2.2"/><circle cx="870" cy="36" r="2.2"/><circle cx="884" cy="36" r="2.2"/><circle cx="898" cy="36" r="2.2"/><circle cx="912" cy="36" r="2.2"/>
        <circle cx="828" cy="50" r="2.2"/><circle cx="842" cy="50" r="2.2"/><circle cx="856" cy="50" r="2.2"/><circle cx="870" cy="50" r="2.2"/><circle cx="884" cy="50" r="2.2"/><circle cx="898" cy="50" r="2.2"/>
      </g>
      <!-- dot grid left -->
      <g class="dot-grid" fill="#a9b7c4">
        <circle cx="72" cy="622" r="2.2"/><circle cx="84" cy="622" r="2.2"/>
        <circle cx="72" cy="636" r="2.2"/><circle cx="84" cy="636" r="2.2"/>
        <circle cx="72" cy="650" r="2.2"/><circle cx="84" cy="650" r="2.2"/>
        <circle cx="72" cy="664" r="2.2"/><circle cx="84" cy="664" r="2.2"/>
        <circle cx="72" cy="678" r="2.2"/><circle cx="84" cy="678" r="2.2"/>
        <circle cx="84" cy="692" r="2.2"/>
      </g>

      <!-- sparkle crosses -->
      <g class="sparkle" stroke-width="3.5" stroke-linecap="round">
        <path d="M77 152v22M66 163h22" stroke="var(--white)"/>
        <path d="M777 315v18M768 324h18" stroke="var(--accent-orange)" stroke-width="2.5"/>
        <path d="M142 368v18M133 377h18" stroke="var(--accent-orange)" stroke-width="2.5"/>
        <path d="M880 696v22M869 707h22" stroke="var(--white)"/>
      </g>

      <defs>
        <linearGradient id="card-airfare" x1="0" y1="0" x2="0" y2="1">
          <stop offset="0" stop-color="#f6a43a"/>
          <stop offset="0.6" stop-color="#f47d4a"/>
          <stop offset="1" stop-color="#b34a7c"/>
        </linearGradient>
        <linearGradient id="card-dining" x1="0" y1="0" x2="0" y2="1">
          <stop offset="0" stop-color="#e9338f"/>
          <stop offset="1" stop-color="#b26fdc"/>
        </linearGradient>
        <linearGradient id="card-fitness" x1="0" y1="0" x2="0" y2="1">
          <stop offset="0" stop-color="#fbd360"/>
          <stop offset="0.6" stop-color="#f2b233"/>
          <stop offset="1" stop-color="#f6c94a"/>
        </linearGradient>
        <linearGradient id="card-hotel" x1="0" y1="0" x2="1" y2="0">
          <stop offset="0" stop-color="#1a8f90"/>
          <stop offset="0.5" stop-color="#2aa9a8"/>
          <stop offset="1" stop-color="#5cc7bb"/>
        </linearGradient>
      </defs>

      <!-- fanned reward cards -->
      <g class="reward-cards" role="img" aria-label="Fan of four reward certificate cards: round trip airfare, travel and dining, fitness, and hotel savings">
        <rect x="-95" y="-215" width="190" height="430" rx="12" fill="url(#card-hotel)" transform="translate(702 618) rotate(8)"/>
        <rect x="-95" y="-215" width="190" height="430" rx="12" fill="url(#card-fitness)" transform="translate(539 607) rotate(-4)"/>
        <rect x="-95" y="-215" width="190" height="430" rx="12" fill="url(#card-dining)" transform="translate(400 600) rotate(-18)"/>
        <rect x="-95" y="-215" width="190" height="430" rx="12" fill="url(#card-airfare)" transform="translate(276 622) rotate(-33)"/>
      </g>
    </svg>

    <h1 class="headline">
      <span class="headline__lead">TRIPLE to</span>
      <span class="headline__main">3X YOUR SALES</span>
      <span class="headline__offer">OFFERING FREE SMART DEVICES</span>
      <span class="headline__detail">AS A BONUS FOR BUYING YOUR<br>PRODUCT OR SERVICE</span>
    </h1>

    <div class="cta-band"></div>
    <a class="cta-button">START A RISK FREE TRIAL</a>
  </main>
</body>
</html>
```